・ターゲット
美容室は銀座にあり、客層は20代~50代の女性です。
メインターゲットは30代です。

・サイトの色
白がベースでブラック、グレーで洗練された
透明感を表現してください。

「シンプルで美しく、魅力的なデザインでかつ予約導線がよいサイト」
を目指しています。

ラフデザイン案がありますので、
レイアウトは基本的にラフデザインをベースにしていただき、
ユーザビリティ的によりよくなる提案があれば理由とともに
アレンジしてください。

ロゴ、使用素材はお渡しします。
1ページ
白、グレー、黒
• フォトショップ形式 (.psd)
• PNG形式 (.png)
提案数が想定よりも少ないため延長させていただきます。参加報酬も4件に増やさせていただきました。
たくさんのご応募ありがとうございます。
トップの表記では選定期限が1/31までとなっておりますが、
現在、最終選定期限を2/5になっております。

期限までには当選対象者にご連絡できるかと思いますのでよろしくお願いします。
現在、候補のランサー様に修正依頼を投げています。
最終選定期限を再度、延長していただいています。

長くなってしまい申し訳ございませんが今しばらくお待ちください。

素材の魅力を最大限に引き出していただけたところが、クライアントに気に入っていただけたポイントでした。ありがとうございます。

たくさんのご提案ありがとうございました。

言葉足らずの点もあったと思いますが、言語外の意図を読み取っていただけて、これほど多様なデザインの提案をいただけるとは思っていませんでした。

たくさんの中から絞り込むのはとても大変な作業で、時間もかかってしまい申し訳ありませんでした。お選びできなかった皆様に申し訳ない気持ちでいっぱいです。
また、このような機会がありましたら、何卒よろしくお願いいたします。

```html
<!DOCTYPE html>
<html lang="ja">
<head>
<meta charset="utf-8">
<title>Atelier Lys | Ginza Hair Salon</title>
<link rel="stylesheet" href="https://fonts.googleapis.com/css2?family=Great+Vibes&family=Lato:wght@400;700&family=Noto+Sans+JP:wght@400;700&display=swap">
<style>
:root{
  --ink:#222;
  --text:#555;
  --muted:#999;
  --line:#d6d6d6;
  --paper:#fff;
  --band:#e9e9e9;
  --photo-a:#e2e2e2;
  --photo-b:#7a7a7a;
  --dark:#2b2b2b;
  --gold:#b08a3c;
}
*{box-sizing:border-box;margin:0;padding:0}
html,body{width:1200px;height:3952px;overflow:hidden}
body{background:var(--paper);color:var(--text);font-family:"Noto Sans JP",sans-serif;font-size:13px;position:relative}
a{text-decoration:none;color:inherit}
.abs{position:absolute}

/* hero */
.hero{left:0;top:0;width:1200px;height:640px;
  background:
    radial-gradient(ellipse 180px 260px at 640px 300px,#2e2e2e 0%,#4a4a4a 45%,rgba(90,90,90,0) 100%),
    radial-gradient(ellipse 260px 200px at 820px 520px,#5a5a5a 0%,rgba(120,120,120,0) 100%),
    radial-gradient(ellipse 220px 300px at 1020px 260px,#9b9b9b 0%,rgba(180,180,180,0) 100%),
    linear-gradient(90deg,#fafafa 0%,#ececec 30%,#bdbdbd 52%,#d8d8d8 78%,#c4c4c4 100%)}
.hero-brand{left:24px;top:20px;width:96px;height:100px;background:var(--dark);color:#fff;display:flex;align-items:flex-end;justify-content:center;padding-bottom:14px;font-size:13px;font-family:"Lato",sans-serif;letter-spacing:1px}
.hero-season{left:160px;top:24px;font-family:"Lato",sans-serif;font-size:13px;color:var(--text);letter-spacing:2px}
.hero-season span{display:block;margin-top:30px;font-size:14px;color:var(--muted);letter-spacing:1px}

/* nav */
.nav{left:90px;top:662px;width:1020px;display:flex;justify-content:space-between;border-top:1px solid var(--line);padding-top:6px}
.nav a{color:var(--ink);font-family:"Lato",sans-serif;font-size:14px;letter-spacing:1px;text-align:center}
.nav a small{display:block;font-size:9px;color:var(--muted);font-family:"Noto Sans JP",sans-serif;margin-top:2px}

/* section heading */
.heading{left:90px;width:1020px;height:64px;display:flex;align-items:center;gap:14px}
.heading .mark{width:44px;height:52px;background:var(--dark);flex:none}
.heading h2{font-family:"Great Vibes",cursive;font-weight:400;font-size:46px;color:var(--ink);white-space:nowrap}
.heading .rule{flex:1;height:1px;background:var(--line)}

/* real hair */
.styles{left:100px;width:1020px;display:grid;grid-template-columns:repeat(5,180px);column-gap:30px}
.style-card{text-align:center;position:relative}
.style-photo{width:180px;height:270px;background:
  radial-gradient(ellipse 60px 90px at 50% 40%,#5c5c5c 0%,rgba(90,90,90,0) 100%),
  linear-gradient(180deg,var(--photo-a),#c9c9c9 60%,var(--photo-b))}
.style-card p{font-family:"Lato",sans-serif;font-size:12px;color:var(--text);margin-top:10px;letter-spacing:1px}
.style-detail{position:absolute;left:0;top:110px;width:180px;height:160px;background:rgba(255,255,255,.88);padding:12px 14px;text-align:left;font-size:10px;line-height:1.7;color:var(--text)}
.style-detail dl{display:grid;grid-template-columns:70px 1fr}
.style-detail dd{color:var(--ink)}
.style-detail .book{display:block;margin-top:8px;background:var(--dark);color:#fff;text-align:center;font-family:"Lato",sans-serif;font-size:9px;letter-spacing:1px;padding:3px 0}
.more{right:90px;top:1520px;font-size:11px;color:var(--muted)}

/* stylists */
.stylists{left:100px;width:1000px;display:grid;grid-template-columns:repeat(5,200px)}
.stylist{text-align:center}
.stylist .face{width:168px;height:168px;border-radius:50%;margin:0 auto;background:radial-gradient(circle at 50% 45%,#6a6a6a 0%,#9a9a9a 30%,#e6e6e6 62%,#d0d0d0 100%)}
.stylist .name{font-family:"Lato",sans-serif;font-size:13px;color:var(--ink);margin-top:12px}
.stylist .kana{font-size:10px;color:var(--muted);margin-top:3px}

/* welcome */
.emblem{left:540px;top:2180px;width:120px;height:170px;display:flex;align-items:center;justify-content:center}
.emblem-name{left:0;top:2370px;width:1200px;text-align:center;font-family:"Lato",sans-serif;font-size:30px;color:var(--gold);letter-spacing:2px}
.welcome{left:220px;top:2450px;width:760px;text-align:center;line-height:2}
.welcome h3{font-size:15px;font-weight:400;color:var(--ink);margin-bottom:6px}
.welcome p{font-size:12px}
.interiors{left:120px;top:2640px;width:960px;display:flex;justify-content:space-between}
.interior{width:180px;height:150px;background:linear-gradient(180deg,#3a3a3a,#b59a78)}

/* special */
.news{top:2950px;width:480px}
.news h4{font-size:12px;font-weight:400;color:var(--ink);border-bottom:1px solid var(--line);padding-bottom:6px;margin-bottom:10px}
.news li{list-style:none;font-size:11px;line-height:1.6;padding:5px 0;border-bottom:1px dotted var(--line)}
.news li time{display:block;color:var(--muted);font-family:"Lato",sans-serif}
.reserve{left:340px;top:3270px;width:520px;height:82px;background:linear-gradient(90deg,#8a7a5e,#c9b48a,#8a7a5e);display:flex;align-items:center;justify-content:space-between;padding:0 30px;color:#fff}
.reserve strong{font-family:"Lato",sans-serif;font-size:30px;letter-spacing:4px;font-weight:700}
.reserve span{font-size:13px}
.buttons{left:100px;top:3392px;width:1020px;display:flex;justify-content:space-between}
.buttons a{width:300px;height:48px;border:1px solid var(--line);display:flex;align-items:center;justify-content:center;color:var(--ink);font-size:13px}

/* footer */
.footer{left:0;top:3480px;width:1200px;height:472px;background:var(--band)}
.info{left:100px;top:3590px;width:520px;font-size:11px;line-height:1.75}
.info .shop{font-family:"Lato",sans-serif;font-size:20px;color:var(--ink);margin-bottom:8px}
.social{left:780px;top:3598px;width:360px;height:260px;background:var(--paper);border:1px solid var(--line)}
.social-head{height:30px;background:#dcdcdc;font-size:11px;color:var(--ink);padding:7px 10px;font-family:"Lato",sans-serif}
.social-body{padding:12px;font-size:11px}
.social-thumbs{display:grid;grid-template-columns:repeat(6,46px);gap:8px;margin-top:14px}
.social-thumbs i{display:block;width:46px;height:46px;background:#c8c8c8}
.copy{left:0;top:3922px;width:1200px;text-align:center;font-family:"Lato",sans-serif;font-size:10px;color:var(--muted)}
</style>
</head>
<body>

<div class="abs hero" role="img" aria-label="Black and white fashion portrait of a model with long wavy hair resting on her arm"></div>
<div class="abs hero-brand">Atelier Lys</div>
<div class="abs hero-season">2013A/W COLLECTION<span>&lsaquo; &nbsp;&nbsp;&nbsp;&nbsp;&nbsp; &rsaquo;</span></div>

<nav class="abs nav">
  <a href="#">HOME<small>ホーム</small></a>
  <a href="#">INFORMATION/PRESS<small>お知らせ</small></a>
  <a href="#">STYLIST<small>スタイリスト</small></a>
  <a href="#">CATALOG<small>カタログ</small></a>
  <a href="#">ACCESS<small>アクセス</small></a>
  <a href="#">PRICE<small>料金</small></a>
  <a href="#">CONTACT<small>お問合せ</small></a>
  <a href="#">RECRUIT<small>求人</small></a>
  <a href="#">RESERVATION<small>ご予約</small></a>
</nav>

<div class="abs heading" style="top:756px"><span class="mark"></span><h2>/ Real Hair /</h2><span class="rule"></span></div>

<div class="abs styles" style="top:836px">
  <div class="style-card"><div class="style-photo" role="img" aria-label="Hairstyle photo: short bob"></div>
    <div class="style-detail">
      <dl><dt>STYLIST</dt><dd>青木 蓮</dd><dt>MENU</dt><dd>カット</dd><dt>LENGTH</dt><dd>ショート</dd><dt>COLOR</dt><dd>ブラウン</dd></dl>
      <a class="book" href="#">RESERVATION</a>
    </div>
    <p>SHORT BOB</p></div>
  <div class="style-card"><div class="style-photo" role="img" aria-label="Hairstyle photo: long waves"></div><p>HAIR STYLE</p></div>
  <div class="style-card"><div class="style-photo" role="img" aria-label="Hairstyle photo: dark bob"></div><p>HAIR STYLE</p></div>
  <div class="style-card"><div class="style-photo" role="img" aria-label="Hairstyle photo: medium curls"></div><p>HAIR STYLE</p></div>
  <div class="style-card"><div class="style-photo" role="img" aria-label="Hairstyle photo: soft bob"></div><p>HAIR STYLE</p></div>
</div>
<div class="abs styles" style="top:1188px">
  <div class="style-card"><div class="style-photo" role="img" aria-label="Hairstyle photo: short cut"></div><p>HAIR STYLE</p></div>
  <div class="style-card"><div class="style-photo" role="img" aria-label="Hairstyle photo: long straight"></div><p>HAIR STYLE</p></div>
  <div class="style-card"><div class="style-photo" role="img" aria-label="Hairstyle photo: side swept"></div><p>HAIR STYLE</p></div>
  <div class="style-card"><div class="style-photo" role="img" aria-label="Hairstyle photo: layered medium"></div><p>HAIR STYLE</p></div>
  <div class="style-card"><div class="style-photo" role="img" aria-label="Hairstyle photo: blonde short"></div><p>HAIR STYLE</p></div>
</div>
<div class="abs more">スタイル一覧へ &rsaquo;</div>

<div class="abs heading" style="top:1564px"><span class="mark"></span><h2>/ Stylist /</h2><span class="rule"></span></div>

<div class="abs stylists" style="top:1652px">
  <div class="stylist"><div class="face" role="img" aria-label="Stylist portrait"></div><p class="name">Ren Aoki</p><p class="kana">青木 蓮</p></div>
  <div class="stylist"><div class="face" role="img" aria-label="Stylist portrait"></div><p class="name">Mio Hanada</p><p class="kana">花田 美緒</p></div>
  <div class="stylist"><div class="face" role="img" aria-label="Stylist portrait"></div><p class="name">Kaito Mori</p><p class="kana">森 海斗</p></div>
  <div class="stylist"><div class="face" role="img" aria-label="Stylist portrait"></div><p class="name">Yuna Saeki</p><p class="kana">佐伯 結菜</p></div>
  <div class="stylist"><div class="face" role="img" aria-label="Stylist portrait"></div><p class="name">Rina Okabe</p><p class="kana">岡部 里奈</p></div>
</div>
<div class="abs stylists" style="top:1912px">
  <div class="stylist"><div class="face" role="img" aria-label="Stylist portrait"></div><p class="name">Sota Ueno</p><p class="kana">上野 蒼太</p></div>
  <div class="stylist"><div class="face" role="img" aria-label="Stylist portrait"></div><p class="name">Kenji Arai</p><p class="kana">新井 健二</p></div>
  <div class="stylist"><div class="face" role="img" aria-label="Stylist portrait"></div><p class="name">Haru Nishi</p><p class="kana">西 陽</p></div>
  <div class="stylist"><div class="face" role="img" aria-label="Stylist portrait"></div><p class="name">Shun Takagi</p><p class="kana">高木 駿</p></div>
  <div class="stylist"><div class="face" role="img" aria-label="Stylist portrait"></div><p class="name">Jun Odaka</p><p class="kana">尾高 純</p></div>
</div>

<div class="abs emblem">
  <svg width="110" height="110" viewBox="0 0 110 110"><circle cx="55" cy="55" r="52" fill="#b08a3c"/></svg>
</div>
<div class="abs emblem-name">Atelier Lys</div>
<div class="abs welcome">
  <h3>Atelier Lysへようこそ！</h3>
  <p>Atelier Lysは銀座の街に、フランスの上質な空間と技術をお届けするサロンとして誕生しました。<br>
  スタイルは大人の女性のための上品で透明感のあるデザインを大切にしています。<br>
  経験豊かなスタイリストが一人ひとりの髪質とライフスタイルに寄り添いご提案します。<br>
  落ち着いた空間で特別なひとときをお過ごしください。スタッフ一同お待ちしております。</p>
</div>
<div class="abs interiors">
  <div class="interior" role="img" aria-label="Salon entrance interior"></div>
  <div class="interior" role="img" aria-label="Salon styling chairs"></div>
  <div class="interior" role="img" aria-label="Salon shampoo area"></div>
  <div class="interior" role="img" aria-label="Salon lounge with warm lighting"></div>
</div>

<div class="abs heading" style="top:2868px"><span class="mark"></span><h2>/ Special /</h2><span class="rule"></span></div>

<div class="abs news" style="left:100px">
  <h4>RANKING ／ 人気スタイルランキング</h4>
  <ul>
    <li><time>2014.03.06</time>春の新作スタイルを公開しました！</li>
    <li><time>2014.03.02</time>雑誌掲載スタイルがランキング入りしました！</li>
    <li><time>2014.02.24</time>人気のショートボブ特集を掲載しました！</li>
    <li><time>2014.02.18</time>冬のカラーランキングを更新しました！</li>
  </ul>
</div>
<div class="abs news" style="left:640px">
  <h4>MEDIA / PRESS / INFORMATION</h4>
  <ul>
    <li><time>2014.03.05</time>雑誌に当店が掲載されました！</li>
    <li><time>2014.02.28</time>営業時間変更のお知らせです。</li>
    <li><time>2014.02.20</time>新メニューの受付を開始しました！</li>
    <li><time>2014.02.12</time>スタッフ募集のお知らせです。</li>
  </ul>
</div>

<a class="abs reserve" href="#"><strong>RESERVATION</strong><span>オンライン予約はこちら</span></a>

<div class="abs buttons">
  <a href="#">よくある質問・お問い合わせ</a>
  <a href="#">会社概要</a>
  <a href="#">採用情報</a>
</div>

<div class="abs footer"></div>
<div class="abs heading" style="top:3488px"><span class="mark"></span><h2>/ Salon Information /</h2><span class="rule"></span></div>
<div class="abs info">
  <p class="shop">atelier lys</p>
  <p>住所<br>東京都中央区銀座1-2-3 ルミエールビル4階</p>
  <p>電話<br>03-0000-0000</p>
  <p>営業時間<br>平日 11:00-21:00 ／ 土日祝 10:00-19:00</p>
  <p>定休日<br>毎週火曜日</p>
  <p>お支払い<br>各種クレジットカードをご利用いただけます。</p>
  <p>ご予約はお電話またはオンライン予約にて承ります。</p>
</div>
<div class="abs social">
  <div class="social-head">Social</div>
  <div class="social-body">
    <p>atelier lys ginza</p>
    <p style="color:var(--muted);margin-top:4px">1,280人がフォローしています</p>
    <div class="social-thumbs"><i></i><i></i><i></i><i></i><i></i><i></i><i></i><i></i><i></i><i></i><i></i><i></i></div>
  </div>
</div>
<p class="abs copy">&copy; ATELIER LYS ALL RIGHTS RESERVED.</p>

</body>
</html>
```